Health & Nutrition - Business Cards

Needs to look new-age, simple, and elegant. The cards are for my services/counsel in health and nutrition - which include mind, body, and soul. I would like to see something clean and simple but beautiful. Can have a plain background or with a pattern but I don't want it to take away from my contact details. Therefore, my info can be on the back of the card and a nice front design. I really like the flower of life symbol. The name of my business is called Willow Lantern.

Target Market(s)

Clients - men & women age 20-60. Adults, parents, teachers, sick individuals seeking nutrient counseling and dietary management.

Industry/Entity Type

Nutritionist

Contact Information for Business Card

Tomas Brindle
Cell: 345-582-7046
Email: tbrindle@mailvane.net

Colors
33a6d7
33b8a4
add136
ffffff
5c5c5c
f04a50
fbee3f
cedeed
85cae6

Requirements
Nice to have
• Maybe it can have some sort of sacred geometry as well, but not required. Nice to have the colors that I choose in the project but feel free to come up with your own use of colors. Thanks! =)

```html
<!DOCTYPE html>
<html lang="en">
<head>
<meta charset="utf-8">
<title>Health &amp; Nutrition – Business Cards</title>
<link rel="stylesheet" href="https://fonts.googleapis.com/css2?family=Figtree:wght@400;600;700&display=swap">
<style>
  :root {
    --stage: #1f1f1e;
    --lime: #add136;
    --lime-soft: #bcd85e;
    --lime-text: #b5d34a;
    --ink: #333333;
    --ink-soft: #3c3c3c;
    --white: #ffffff;
  }
  * { box-sizing: border-box; margin: 0; padding: 0; }
  html, body { width: 1200px; height: 1000px; overflow: hidden; }
  body {
    background: var(--stage);
    font-family: "Figtree", Arial, sans-serif;
    position: relative;
  }
  .card {
    position: absolute;
    left: 259px;
    width: 682px;
    height: 456px;
    overflow: hidden;
  }
  .card--front { top: 35px; }
  .card--back { top: 509px; height: 457px; }
  .card__art { position: absolute; inset: 0; width: 100%; height: 100%; display: block; }

  .brand { position: absolute; display: flex; flex-direction: column; align-items: center; }
  .brand__mark { border-style: solid; transform: rotate(45deg); }
  .brand__name { white-space: nowrap; }

  .card--front .brand { left: 0; right: 0; top: 150px; }
  .card--front .brand__mark { width: 72px; height: 72px; border-width: 3px; border-color: var(--white); margin-bottom: 38px; }
  .card--front .brand__name { color: var(--white); font-size: 41px; font-weight: 400; letter-spacing: 0.2px; }

  .card--back .brand { left: 70px; width: 260px; top: 106px; }
  .card--back .brand__mark { width: 54px; height: 54px; border-width: 2.5px; border-color: var(--lime-text); margin-bottom: 28px; }
  .card--back .brand__name { color: var(--lime-text); font-size: 24px; font-weight: 700; }

  .divider { position: absolute; left: 356px; top: 84px; width: 1.5px; height: 208px; background: var(--lime); }

  .contact { position: absolute; left: 411px; top: 136px; color: var(--ink-soft); }
  .contact__name { font-size: 19px; font-weight: 700; color: var(--ink); margin-bottom: 14px; }
  .contact__row { display: flex; align-items: center; gap: 7px; font-size: 15px; height: 24px; margin-bottom: 13px; margin-left: 0; }
  .contact__icon { width: 23px; height: 23px; flex: none; }
</style>
</head>
<body>

<section class="card card--front">
  <svg class="card__art" viewBox="0 0 682 456" preserveAspectRatio="none" aria-hidden="true">
    <defs>
      <linearGradient id="frontBase" x1="0" y1="0" x2="1" y2="1">
        <stop offset="0" stop-color="#bfdb66"/>
        <stop offset="0.55" stop-color="#add136"/>
        <stop offset="1" stop-color="#a6cc2e"/>
      </linearGradient>
    </defs>
    <rect width="682" height="456" fill="url(#frontBase)"/>
    <path d="M0,0 H175 C120,120 190,250 330,320 C430,370 560,420 682,456 H0 Z" fill="#ffffff" opacity="0.12"/>
    <path d="M0,220 C90,300 230,400 420,456 H0 Z" fill="#ffffff" opacity="0.12"/>
    <path d="M0,360 C20,300 70,250 120,210 L0,210 Z" fill="#ffffff" opacity="0.06"/>
    <path d="M515,0 C500,160 560,330 650,456 H682 V0 Z" fill="#ffffff" opacity="0.14"/>
    <path d="M175,0 C250,110 300,140 420,180 L682,260 V0 Z" fill="#ffffff" opacity="0.06"/>
  </svg>
  <div class="brand">
    <div class="brand__mark"></div>
    <div class="brand__name">Health &amp; Nutrition</div>
  </div>
</section>

<section class="card card--back">
  <svg class="card__art" viewBox="0 0 682 457" preserveAspectRatio="none" aria-hidden="true">
    <defs>
      <linearGradient id="backGrey" x1="0" y1="0" x2="1" y2="0.4">
        <stop offset="0" stop-color="#ffffff"/>
        <stop offset="0.6" stop-color="#eceded"/>
        <stop offset="1" stop-color="#dedfe0"/>
      </linearGradient>
      <linearGradient id="backLime" x1="0" y1="0" x2="1" y2="0">
        <stop offset="0" stop-color="#c2dc6a"/>
        <stop offset="1" stop-color="#afd23a"/>
      </linearGradient>
    </defs>
    <rect width="682" height="457" fill="#fbfbfb"/>
    <path d="M260,0 C400,120 520,240 600,380 L682,380 V0 Z" fill="url(#backGrey)"/>
    <path d="M420,0 C520,90 600,220 682,330 V0 Z" fill="#ffffff"/>
    <path d="M0,145 C200,150 360,230 500,380 H0 Z" fill="#e9eaea" opacity="0.8"/>
    <path d="M0,320 C140,296 260,300 380,340 C480,372 580,380 682,346 V457 H0 Z" fill="#d6e99a"/>
    <path d="M0,328 C150,305 270,316 400,360 C500,392 600,400 682,372 V457 H0 Z" fill="url(#backLime)"/>
    <path d="M0,340 C130,330 240,370 330,457 H0 Z" fill="#ffffff" opacity="0.15"/>
  </svg>
  <div class="brand">
    <div class="brand__mark"></div>
    <div class="brand__name">Health &amp; Nutrition</div>
  </div>
  <div class="divider"></div>
  <div class="contact">
    <div class="contact__name">Tomas Brindle</div>
    <div class="contact__row">
      <svg class="contact__icon" viewBox="0 0 24 24" aria-hidden="true">
        <circle cx="12" cy="12" r="12" fill="var(--lime)"/>
        <rect x="6" y="8" width="12" height="8.5" rx="1" fill="#fff"/>
        <path d="M6.5,8.6 L12,12.8 L17.5,8.6" fill="none" stroke="var(--lime)" stroke-width="1.3"/>
      </svg>
      <span>studio@fernquill.com</span>
    </div>
    <div class="contact__row">
      <svg class="contact__icon" viewBox="0 0 24 24" aria-hidden="true">
        <circle cx="12" cy="12" r="12" fill="var(--lime)"/>
        <path d="M8.2,6.2 L10.2,6 L11.2,8.8 L9.9,10 C10.6,11.7 12.1,13.3 13.9,14.1 L15.1,12.8 L17.9,13.8 L17.7,15.8 C17.5,16.9 16.3,17.6 15.2,17.3 C11.1,16.2 7.8,12.9 6.7,8.8 C6.4,7.7 7.1,6.4 8.2,6.2 Z" fill="#fff"/>
      </svg>
      <span>(+351) 284 619 052</span>
    </div>
  </div>
</section>

</body>
</html>
```